Logo for Internal Medicine practice

I want a logo for my Internal Medicine practice, I would like it to be with my name on it which is Lucía Barrenechea Ruiz.

I would like the business card to say the following (it is in Spanish since my practice is in Spanish):

Lucía Barrenechea Ruiz
Medicina Interna
Cel. 5583617204
luciabarrenechearuiz@correovela.mx

Logo Text

Lucía Barrenechea

```html
<!DOCTYPE html>
<html lang="es">
<head>
<meta charset="utf-8">
<title>Lucía Barrenechea – Tarjetas de presentación</title>
<link rel="stylesheet" href="https://fonts.googleapis.com/css2?family=Archivo:wght@400;700&family=Roboto:wght@300;400;500&display=swap">
<style>
  :root {
    --navy: #182852;
    --sky: #6aa6d3;
    --azure: #1b95d4;
    --rule: #7aa3c9;
    --paper: #ffffff;
    --backdrop: #eef2ea;
  }
  * { box-sizing: border-box; margin: 0; padding: 0; }
  html, body { width: 1200px; height: 1200px; overflow: hidden; }
  body {
    background: var(--backdrop);
    position: relative;
    font-family: "Roboto", Arial, sans-serif;
  }
  .card {
    position: absolute;
    top: 503px;
    width: 420px;
    height: 240px;
    overflow: hidden;
  }
  .card--front { left: 155px; background: var(--paper); }
  .card--back { left: 623px; background: var(--navy); }

  .brand-dot {
    position: absolute;
    left: 64px; top: 28px;
    width: 44px; height: 44px;
    border-radius: 50%;
    background: var(--azure);
  }
  .brand-name {
    position: absolute;
    left: 17px; top: 104px;
    font-family: "Archivo", Arial, sans-serif;
    font-weight: 700;
    font-size: 13.5px;
    letter-spacing: 0.1px;
    color: var(--navy);
    white-space: nowrap;
  }
  .divider {
    position: absolute;
    left: 17px; top: 178px;
    width: 385px; height: 1px;
    background: var(--rule);
  }
  .holder {
    position: absolute;
    left: 17px; top: 190px;
    line-height: 1;
    white-space: nowrap;
  }
  .holder-name { font-size: 15px; color: var(--navy); font-weight: 400; }
  .holder-name .mid { color: var(--sky); font-weight: 300; }
  .holder-name .last { color: var(--sky); font-weight: 500; }
  .holder-role { margin-top: 4px; font-size: 11px; color: var(--navy); }

  .contact {
    position: absolute;
    right: 17px; top: 195px;
    list-style: none;
    font-size: 11px;
    color: var(--navy);
    text-align: right;
  }
  .contact li {
    display: flex;
    align-items: center;
    justify-content: flex-end;
    gap: 7px;
    height: 14.5px;
  }
  .contact svg { width: 12px; height: 12px; flex: none; }

  .back-disc {
    position: absolute;
    left: -30px; top: 60px;
    width: 150px; height: 150px;
    border-radius: 50%;
    background: linear-gradient(135deg, var(--azure), var(--sky));
  }
  .back-name {
    position: absolute;
    right: 29px; top: 190px;
    font-family: "Archivo", Arial, sans-serif;
    font-weight: 700;
    font-size: 22px;
    color: var(--paper);
    white-space: nowrap;
  }
</style>
</head>
<body>
  <section class="card card--front" aria-label="Frente de la tarjeta">
    <div class="brand-dot"></div>
    <div class="brand-name">LUCÍA BARRENECHEA</div>
    <div class="divider"></div>
    <div class="holder">
      <p class="holder-name">Lucía <span class="mid">Barrenechea</span> <span class="last">Ruiz</span></p>
      <p class="holder-role">Medicina Interna</p>
    </div>
    <ul class="contact">
      <li>
        <span>558.361.7204</span>
        <svg viewBox="0 0 12 12" aria-hidden="true">
          <circle cx="6" cy="6" r="6" fill="var(--sky)"/>
          <rect x="4" y="2.6" width="4" height="6.8" rx="0.8" fill="none" stroke="#fff" stroke-width="0.9"/>
        </svg>
      </li>
      <li>
        <span>luciabarrenechearuiz@correovela.mx</span>
        <svg viewBox="0 0 12 12" aria-hidden="true">
          <circle cx="6" cy="6" r="6" fill="var(--sky)"/>
          <rect x="3" y="3.8" width="6" height="4.4" fill="none" stroke="#fff" stroke-width="0.8"/>
          <path d="M3 3.8 L6 6.3 L9 3.8" fill="none" stroke="#fff" stroke-width="0.8"/>
        </svg>
      </li>
    </ul>
  </section>

  <section class="card card--back" aria-label="Reverso de la tarjeta">
    <div class="back-disc"></div>
    <div class="back-name">LUCÍA BARRENECHEA</div>
  </section>
</body>
</html>
```